Business card design Needed for new logo / Construction business, home extensions and new builds

We need a business card design using our new logo files which i will attach to this project :)

We are a small construction business specialising in home extensions, new builds and property development. We are very ambitious and would appreciate professional and elegant designs for our new business card.

Very serious about using the services on BriefNest and recently acquired our new logo from here :)

Please get involved, i will feedback when i can as i am very busy but can respond daily, thanks

Target Market(s)

People that want to build onto their houses, new building developments or adding too their existing property

Industry/Entity Type

Construction

Contact Information for Business Card

Hollin Marsh Construction, Tobias Renwick (Managing Director), Tel 07822200444, email - info@hollin-marsh, www.hollin-marsh.co.uk

Colors

Designer to choose colors to be used in the design.

Requirements
Must have
• I like a deep grey on the back please. A lot of you have provided black from and back, try mixing things up a little. The black looks cool 😎 Thanks

```html
<!DOCTYPE html>
<html lang="en">
<head>
<meta charset="utf-8">
<title>Hollin Marsh Construction – Business Card</title>
<link rel="stylesheet" href="https://fonts.googleapis.com/css2?family=Montserrat:wght@400;500;700&display=swap">
<style>
  :root {
    --scene-bg: #2b2b2d;
    --front-bg: #141414;
    --back-bg: #3a3a3f;
    --gold: #e0a82e;
    --gold-light: #f4c651;
    --silver: #c9cacc;
    --text-light: #e6e6e8;
  }
  * { box-sizing: border-box; margin: 0; padding: 0; }
  html, body {
    width: 1200px; height: 689px; overflow: hidden;
    background: var(--scene-bg);
    font-family: "Montserrat", sans-serif;
  }
  .sheet {
    position: relative; width: 1200px; height: 689px;
    display: flex; align-items: center; justify-content: center; gap: 40px;
  }
  .card {
    position: relative; width: 540px; height: 309px;
    border-radius: 18px; overflow: hidden;
  }
  .card--front { background: var(--front-bg); }
  .card--back { background: var(--back-bg); }

  .brand {
    position: absolute; display: flex; flex-direction: column; align-items: center; gap: 10px;
    color: var(--gold); font-weight: 700; text-transform: uppercase; text-align: center;
  }
  .brand__mark { width: 18px; height: 18px; background: var(--gold); }
  .brand__name { letter-spacing: 0.08em; line-height: 1.25; }
  .card--front .brand { left: 0; right: 0; top: 96px; }
  .card--front .brand__name { font-size: 28px; }
  .card--back .brand { left: 30px; width: 230px; top: 92px; }
  .card--back .brand__name { font-size: 20px; }

  .divider {
    position: absolute; left: 282px; top: 48px; width: 1.5px; height: 160px;
    background: var(--gold);
  }
  .person { position: absolute; left: 305px; top: 52px; }
  .person__name { color: var(--gold); font-weight: 700; font-size: 21px; }
  .person__role { color: var(--text-light); font-weight: 500; font-size: 12px; margin-top: 3px; }

  .contacts {
    position: absolute; left: 305px; top: 140px; list-style: none;
    color: var(--text-light); font-size: 12px; font-weight: 400;
  }
  .contacts li { display: flex; align-items: center; gap: 7px; margin-bottom: 6px; }
  .contacts svg { width: 11px; height: 11px; flex: none; fill: var(--gold); }

  .bands { position: absolute; left: 0; bottom: 0; width: 540px; height: 60px; }
</style>
</head>
<body>
<main class="sheet">
  <section class="card card--front" aria-label="Card front">
    <div class="brand">
      <span class="brand__mark"></span>
      <span class="brand__name">Hollin Marsh<br>Construction</span>
    </div>
  </section>

  <section class="card card--back" aria-label="Card back">
    <div class="brand">
      <span class="brand__mark"></span>
      <span class="brand__name">Hollin Marsh<br>Construction</span>
    </div>
    <span class="divider"></span>
    <div class="person">
      <p class="person__name">Tobias Renwick</p>
      <p class="person__role">Managing Director</p>
    </div>
    <ul class="contacts">
      <li><svg viewBox="0 0 12 12"><path d="M2 1h3l1 3-1.5 1a7 7 0 0 0 2.5 2.5L8 6l3 1v3c0 .6-.4 1-1 1A9 9 0 0 1 1 2c0-.6.4-1 1-1z"/></svg>07822200444</li>
      <li><svg viewBox="0 0 12 12"><path d="M1 3h10v6H1z M1 3l5 3.5L11 3" stroke="#3a3a3f" stroke-width="0.8"/></svg>info@hollin-marsh</li>
      <li><svg viewBox="0 0 12 12"><circle cx="6" cy="6" r="5"/></svg>www.hollin-marsh.co.uk</li>
    </ul>
    <svg class="bands" viewBox="0 0 540 60" preserveAspectRatio="none" aria-hidden="true">
      <polygon points="0,48 380,48 396,30 540,30 540,60 0,60" fill="#c9cacc"/>
      <polygon points="410,10 540,10 540,60 396,60" fill="#e0a82e"/>
    </svg>
  </section>
</main>
</body>
</html>
```